School learning environment project dashboard

We have an online learning enviroment for schools (12 / 18 year). Within this enviroment students work on projects.

Attached we have a setup we have created for a project, but we are looking for more ideas to make this even better, more sexy and still keep it functional for teachers and students.

The attached files show one dashboard we have. This dashboard holds the roadmap for the student, upcoming appointments, latest messages and the main documents the student is working on.

Target Market(s)

schools

Number of Pages Required

1 page

Font styles to use
Sans Serif

```html
<!DOCTYPE html>
<html lang="en">
<head>
<meta charset="utf-8">
<title>Learnway – Student Dashboard</title>
<link href="https://fonts.googleapis.com/css2?family=Quicksand:wght@500;600;700&family=Open+Sans:wght@400;600&display=swap" rel="stylesheet">
<style>
:root{
  --navy:#10285a;
  --sidebar:#2b58a0;
  --page:#f6f5f0;
  --card:#ffffff;
  --banner:#13275a;
  --ink:#1b1b1b;
  --line:#e3e3e3;
  --blue:#1d8fe1;
  --yellow:#f7c600;
  --cell:#efefea;
  --purple:#a64ff0;
  --green:#2ec99a;
  --orange:#f39a12;
}
*{box-sizing:border-box;margin:0;padding:0}
html,body{width:1200px;height:818px;overflow:hidden}
body{background:var(--navy);font-family:"Quicksand",sans-serif;color:var(--ink);position:relative}
.sidebar{position:absolute;left:48px;top:47px;width:250px;height:738px;background:var(--sidebar);color:#fff}
.brand{position:absolute;left:0;right:0;top:37px;text-align:center;font-weight:600;font-size:16px;letter-spacing:.5px}
.nav{position:absolute;left:27px;top:111px;list-style:none}
.nav li{display:flex;align-items:center;height:30px;margin-bottom:34.5px;font-weight:600;font-size:14px}
.nav li:nth-child(3){margin-bottom:36px}
.nav li:nth-child(4){margin-bottom:41px}
.nav svg{width:30px;height:30px;margin-right:10px}
.nav .active span{border-bottom:3px solid var(--yellow);padding-bottom:1px}
.laptop-visual{position:absolute;left:22px;top:583px;width:263px;height:136px;border-radius:8px 8px 4px 4px;background:linear-gradient(180deg,#e9edf3 0%,#c9ccd2 80%,#a9acb2 100%);z-index:2}
.main{position:absolute;left:298px;top:47px;width:859px;height:738px;background:var(--page)}
.title{position:absolute;left:34px;top:36px;font-size:23px;font-weight:700;letter-spacing:.3px}
.toplinks{position:absolute;left:569px;top:32px;display:flex;gap:28px;font-size:16px;font-weight:500}
.toplinks a{display:flex;align-items:center;gap:5px;color:var(--ink);text-decoration:none}
.banner{position:absolute;left:34px;top:100px;width:499px;height:162px;background:var(--banner);color:#fff}
.banner h2{position:absolute;left:20px;top:22px;font-size:15px;font-weight:700}
.banner p{position:absolute;left:21px;top:57px;width:380px;font-size:13.5px;line-height:18px;font-weight:500}
.banner .more{position:absolute;left:21px;top:119px;font-size:13px;font-weight:500}
.banner-visual{position:absolute;left:258px;top:10px;width:262px;height:152px;background:linear-gradient(135deg,#f1923a 0%,#c96b2a 45%,#2a2a35 100%);opacity:.9}
.card{position:absolute;background:var(--card);border-radius:4px}
.docs{left:33px;top:302px;width:500px;height:385px}
.docs h3{position:absolute;left:20px;top:18px;font-size:14.5px;font-weight:500;letter-spacing:.3px}
.doc-list{position:absolute;left:20px;top:55px;width:431px;list-style:none}
.doc{height:51.8px;display:flex;align-items:center;border-bottom:1px solid var(--line);font-size:14px;font-weight:500}
.doc:last-child{border-bottom:none}
.doc .kind{width:47px;display:flex;justify-content:center}
.doc .name{flex:1}
.doc .actions{display:flex;gap:12px;margin-right:14px}
.doc .actions svg{width:17px;height:17px}
.calendar{left:559px;top:99px;width:227px;height:192px;border-radius:8px;padding:12px 14px}
.cal-head{display:flex;justify-content:space-between;align-items:center}
.cal-head strong{font-size:11px;font-weight:700;color:#444}
.cal-head span{font-size:8.5px;color:#666;font-weight:600}
.cal-grid{display:grid;grid-template-columns:repeat(7,18px);column-gap:10.2px;row-gap:8px;margin-top:6px}
.cal-grid b{font-size:7px;font-weight:600;color:#555;text-align:center}
.cal-grid i{font-style:normal;height:18px;border-radius:3px;background:var(--cell);font-size:7px;color:#555;display:flex;align-items:center;justify-content:center}
.cal-grid i.out{color:#999}
.cal-grid i.purple{background:var(--purple);color:#fff}
.cal-grid i.green{background:var(--green);color:#fff}
.cal-grid i.orange{background:var(--orange);color:#fff}
.quick-visual{position:absolute;left:562px;top:304px;width:208px;height:180px;background:linear-gradient(180deg,#f1f1ee 0%,#e2e3e6 70%,#cfd1d4 100%)}
.quick-links{position:absolute;left:580px;top:315px;list-style:none}
.quick-links li{display:flex;align-items:center;gap:6px;font-family:"Open Sans",sans-serif;font-size:12px;height:22px}
.quick-links li span{text-decoration:underline}
.quick-links li svg{width:14px;height:10px}
.profile{left:559px;top:503px;width:227px;height:185px;border-radius:8px}
.avatar{position:absolute;left:16px;top:12px;width:44px;height:44px;border-radius:50%;background:radial-gradient(circle at 50% 40%,#c9a58c,#5c6e6a)}
.profile h4{position:absolute;left:67px;top:19px;font-size:13.5px;font-weight:500}
.profile .role{position:absolute;left:67px;top:38px;font-size:10.5px;font-weight:500}
.dots{position:absolute;right:18px;top:14px;width:18px}
.contact{position:absolute;left:19px;top:61px;display:flex;gap:18px}
.contact span{width:30px;height:25px;border-radius:13px;background:#f1f1ee;display:flex;align-items:center;justify-content:center}
.contact svg{width:11px;height:11px}
.profile hr{position:absolute;left:16px;right:16px;top:98px;border:none;border-top:1px solid var(--line)}
.profile p{position:absolute;left:10px;top:120px;width:212px;font-family:"Open Sans",sans-serif;font-size:10px;line-height:13px}
.copyright{position:absolute;left:587px;top:709px;font-family:"Open Sans",sans-serif;font-size:8.8px;color:#333}
</style>
</head>
<body>
<aside class="sidebar">
  <div class="brand">LEARNWAY</div>
  <ul class="nav">
    <li class="active"><svg viewBox="0 0 30 30"><rect x="3" y="6" width="24" height="16" rx="2" fill="#e8e8e8" stroke="#555"/><rect x="6" y="9" width="7" height="9" fill="#f39a12"/><rect x="15" y="10" width="9" height="2" fill="#e24a3b"/><rect x="15" y="14" width="7" height="2" fill="#555"/><rect x="11" y="22" width="8" height="3" fill="#777"/></svg><span>Dashboard</span></li>
    <li><svg viewBox="0 0 30 30"><path d="M15 4 L27 15 L15 26 L3 15 Z" fill="#2a2a2a"/><circle cx="15" cy="12" r="4" fill="#d9a066"/><path d="M9 21 Q15 15 21 21 Z" fill="#c0463a"/></svg><span>Profile</span></li>
    <li><svg viewBox="0 0 30 30"><rect x="4" y="9" width="22" height="16" rx="2" fill="#f5a623"/><rect x="11" y="5" width="8" height="5" rx="1" fill="none" stroke="#c98212" stroke-width="2"/><rect x="4" y="15" width="22" height="2" fill="#d48a14"/></svg><span>Projects</span></li>
    <li><svg viewBox="0 0 30 30"><circle cx="15" cy="15" r="13" fill="#f7c02c"/><rect x="8" y="11" width="10" height="8" rx="1" fill="#333"/><path d="M18 13 L23 10 L23 20 L18 17 Z" fill="#333"/></svg><span>Online</span></li>
    <li><svg viewBox="0 0 30 30"><circle cx="15" cy="15" r="13" fill="#f7c02c"/><rect x="10.5" y="7" width="9" height="16" rx="2" fill="#333"/><rect x="12" y="9" width="6" height="11" fill="#7fc4f0"/></svg><span>App</span></li>
  </ul>
  <div class="laptop-visual" role="img" aria-label="Laptop illustration showing the dashboard with charts"></div>
</aside>

<main class="main">
  <h1 class="title">DASHBOARD</h1>
  <nav class="toplinks">
    <a href="#"><svg width="20" height="20" viewBox="0 0 20 20"><circle cx="10" cy="10" r="6" fill="#f7c600" stroke="#222" stroke-width="1.5"/><g stroke="#222" stroke-width="1.5"><path d="M10 1v3M10 16v3M1 10h3M16 10h3M3.6 3.6l2 2M14.4 14.4l2 2M3.6 16.4l2-2M14.4 5.6l2-2"/></g></svg>Opportunities</a>
    <a href="#"><svg width="19" height="19" viewBox="0 0 20 20"><circle cx="10" cy="10" r="8.5" fill="#f7c600" stroke="#222" stroke-width="1.5"/><text x="10" y="14.5" text-anchor="middle" font-size="12" font-weight="700" font-family="Quicksand,sans-serif" fill="#222">?</text></svg>Help</a>
  </nav>

  <section class="banner">
    <div class="banner-visual" role="img" aria-label="Illustration of a student working on a laptop at a desk"></div>
    <h2>Hello Mateo!</h2>
    <p>You have 9 projects pending and have an Online Schedule on September 23 at 9:00 am.</p>
    <span class="more">read more...</span>
  </section>

  <section class="card docs">
    <h3>DOCUMENTS</h3>
    <ul class="doc-list">
      <li class="doc"><span class="kind"><svg width="26" height="34" viewBox="0 0 26 34"><path d="M4 6 L20 2 L24 28 L8 32 Z" fill="#2f6fc6"/><path d="M4 6 L8 32 L5 32 L2 8 Z" fill="#1d4f9a"/><rect x="12" y="13" width="6" height="4" fill="#cfe1f7" transform="rotate(-12 15 15)"/></svg></span><span class="name">Project 101</span><span class="actions"><svg viewBox="0 0 16 16"><path d="M8 1v9M4 6l4 4 4-4M2 14h12" stroke="var(--blue)" stroke-width="2.4" fill="none"/></svg><svg viewBox="0 0 16 16"><path d="M8 11V2M4 6l4-4 4 4M2 14h12" stroke="var(--blue)" stroke-width="2.4" fill="none"/></svg><svg viewBox="0 0 16 16"><path d="M1 3h5l1.5 1.5H14V7H3.5L1 13Z" fill="var(--blue)"/><path d="M3.5 8H16l-2.5 6H1Z" fill="var(--blue)"/></svg></span></li>
      <li class="doc"><span class="kind"><svg width="38" height="26" viewBox="0 0 38 26"><path d="M2 18 L20 24 L36 16 L18 10 Z" fill="none" stroke="#2f6fc6" stroke-width="1.5"/><path d="M4 14 L20 20 L34 12 L18 6 Z" fill="#fff" stroke="#2f6fc6" stroke-width="1.5"/><path d="M8 10 L22 16 L32 8 L18 2 Z" fill="#fff" stroke="#2f6fc6" stroke-width="1.5"/></svg></span><span class="name">Paper works</span><span class="actions"><svg viewBox="0 0 16 16"><path d="M8 1v9M4 6l4 4 4-4M2 14h12" stroke="var(--blue)" stroke-width="2.4" fill="none"/></svg><svg viewBox="0 0 16 16"><path d="M8 11V2M4 6l4-4 4 4M2 14h12" stroke="var(--blue)" stroke-width="2.4" fill="none"/></svg><svg viewBox="0 0 16 16"><path d="M1 3h5l1.5 1.5H14V7H3.5L1 13Z" fill="var(--blue)"/><path d="M3.5 8H16l-2.5 6H1Z" fill="var(--blue)"/></svg></span></li>
      <li class="doc"><span class="kind"><svg width="26" height="34" viewBox="0 0 26 34"><path d="M4 6 L20 2 L24 28 L8 32 Z" fill="#2f6fc6"/><path d="M4 6 L8 32 L5 32 L2 8 Z" fill="#1d4f9a"/><rect x="12" y="13" width="6" height="4" fill="#cfe1f7" transform="rotate(-12 15 15)"/></svg></span><span class="name">Project 101</span><span class="actions"><svg viewBox="0 0 16 16"><path d="M8 1v9M4 6l4 4 4-4M2 14h12" stroke="var(--blue)" stroke-width="2.4" fill="none"/></svg><svg viewBox="0 0 16 16"><path d="M8 11V2M4 6l4-4 4 4M2 14h12" stroke="var(--blue)" stroke-width="2.4" fill="none"/></svg><svg viewBox="0 0 16 16"><path d="M1 3h5l1.5 1.5H14V7H3.5L1 13Z" fill="var(--blue)"/><path d="M3.5 8H16l-2.5 6H1Z" fill="var(--blue)"/></svg></span></li>
      <li class="doc"><span class="kind"><svg width="38" height="26" viewBox="0 0 38 26"><path d="M2 18 L20 24 L36 16 L18 10 Z" fill="none" stroke="#2f6fc6" stroke-width="1.5"/><path d="M4 14 L20 20 L34 12 L18 6 Z" fill="#fff" stroke="#2f6fc6" stroke-width="1.5"/><path d="M8 10 L22 16 L32 8 L18 2 Z" fill="#fff" stroke="#2f6fc6" stroke-width="1.5"/></svg></span><span class="name">Paper works</span><span class="actions"><svg viewBox="0 0 16 16"><path d="M8 1v9M4 6l4 4 4-4M2 14h12" stroke="var(--blue)" stroke-width="2.4" fill="none"/></svg><svg viewBox="0 0 16 16"><path d="M8 11V2M4 6l4-4 4 4M2 14h12" stroke="var(--blue)" stroke-width="2.4" fill="none"/></svg><svg viewBox="0 0 16 16"><path d="M1 3h5l1.5 1.5H14V7H3.5L1 13Z" fill="var(--blue)"/><path d="M3.5 8H16l-2.5 6H1Z" fill="var(--blue)"/></svg></span></li>
      <li class="doc"><span class="kind"><svg width="26" height="34" viewBox="0 0 26 34"><path d="M4 6 L20 2 L24 28 L8 32 Z" fill="#2f6fc6"/><path d="M4 6 L8 32 L5 32 L2 8 Z" fill="#1d4f9a"/><rect x="12" y="13" width="6" height="4" fill="#cfe1f7" transform="rotate(-12 15 15)"/></svg></span><span class="name">Project 101</span><span class="actions"><svg viewBox="0 0 16 16"><path d="M8 1v9M4 6l4 4 4-4M2 14h12" stroke="var(--blue)" stroke-width="2.4" fill="none"/></svg><svg viewBox="0 0 16 16"><path d="M8 11V2M4 6l4-4 4 4M2 14h12" stroke="var(--blue)" stroke-width="2.4" fill="none"/></svg><svg viewBox="0 0 16 16"><path d="M1 3h5l1.5 1.5H14V7H3.5L1 13Z" fill="var(--blue)"/><path d="M3.5 8H16l-2.5 6H1Z" fill="var(--blue)"/></svg></span></li>
      <li class="doc"><span class="kind"><svg width="38" height="26" viewBox="0 0 38 26"><path d="M2 18 L20 24 L36 16 L18 10 Z" fill="none" stroke="#2f6fc6" stroke-width="1.5"/><path d="M4 14 L20 20 L34 12 L18 6 Z" fill="#fff" stroke="#2f6fc6" stroke-width="1.5"/><path d="M8 10 L22 16 L32 8 L18 2 Z" fill="#fff" stroke="#2f6fc6" stroke-width="1.5"/></svg></span><span class="name">Paper works</span><span class="actions"><svg viewBox="0 0 16 16"><path d="M8 1v9M4 6l4 4 4-4M2 14h12" stroke="var(--blue)" stroke-width="2.4" fill="none"/></svg><svg viewBox="0 0 16 16"><path d="M8 11V2M4 6l4-4 4 4M2 14h12" stroke="var(--blue)" stroke-width="2.4" fill="none"/></svg><svg viewBox="0 0 16 16"><path d="M1 3h5l1.5 1.5H14V7H3.5L1 13Z" fill="var(--blue)"/><path d="M3.5 8H16l-2.5 6H1Z" fill="var(--blue)"/></svg></span></li>
    </ul>
  </section>

  <section class="card calendar">
    <div class="cal-head"><strong>Calendar</strong><span>September 2020 ▾</span></div>
    <div class="cal-grid">
      <b>Mo</b><b>Tu</b><b>We</b><b>Th</b><b>Fr</b><b>Sa</b><b>Su</b>
      <i class="out">31</i><i>1</i><i>2</i><i>3</i><i>4</i><i>5</i><i>6</i>
      <i>7</i><i>8</i><i class="purple">9</i><i>10</i><i>11</i><i>12</i><i>13</i>
      <i>14</i><i>15</i><i>16</i><i class="green">17</i><i class="green">18</i><i>19</i><i>20</i>
      <i>21</i><i>22</i><i class="orange">23</i><i>24</i><i>25</i><i>26</i><i>27</i>
      <i>28</i><i>29</i><i>30</i><i class="out">1</i><i class="out">2</i><i class="out">3</i><i class="out">4</i>
    </div>
  </section>

  <div class="quick-visual" role="img" aria-label="Illustration of a desktop monitor with a teacher pointing at a small board"></div>
  <ul class="quick-links">
    <li><svg viewBox="0 0 14 10"><path d="M0 3.5h8V0l6 5-6 5V6.5H0Z" fill="#111"/></svg><span>Appointments</span></li>
    <li><svg viewBox="0 0 14 10"><path d="M0 3.5h8V0l6 5-6 5V6.5H0Z" fill="#111"/></svg><span>Recent Posts</span></li>
    <li><svg viewBox="0 0 14 10"><path d="M0 3.5h8V0l6 5-6 5V6.5H0Z" fill="#111"/></svg><span>Messages</span></li>
    <li><svg viewBox="0 0 14 10"><path d="M0 3.5h8V0l6 5-6 5V6.5H0Z" fill="#111"/></svg><span>Progress</span></li>
    <li><svg viewBox="0 0 14 10"><path d="M0 3.5h8V0l6 5-6 5V6.5H0Z" fill="#111"/></svg><span>Tools</span></li>
  </ul>

  <section class="card profile">
    <div class="avatar" role="img" aria-label="Student profile photo"></div>
    <h4>Mateo Linares</h4>
    <span class="role">Sophomore</span>
    <svg class="dots" viewBox="0 0 18 4"><circle cx="2" cy="2" r="1.6" fill="#999"/><circle cx="9" cy="2" r="1.6" fill="#999"/><circle cx="16" cy="2" r="1.6" fill="#999"/></svg>
    <div class="contact">
      <span><svg viewBox="0 0 12 12"><path d="M2.5 1 L4.5 1 L5.2 3.5 L4 4.5 Q5 7 7.5 8 L8.5 6.8 L11 7.5 L11 9.5 Q10.5 11 9 11 Q1 10 1 3 Q1 1.5 2.5 1Z" fill="#111"/></svg></span>
      <span><svg viewBox="0 0 12 12"><rect x="1" y="2.5" width="10" height="7" rx="1" fill="#111"/><path d="M1.5 3l4.5 3.5L10.5 3" stroke="#fff" fill="none"/></svg></span>
      <span><svg viewBox="0 0 12 12"><path d="M1 1.5h10v7H4L1.5 11V8.5H1Z" fill="#111"/></svg></span>
    </div>
    <hr>
    <p>Lorem ipsum dolor sit amet, consectetur adipiscing elit, sed do eiusmod tempor incididunt ut labore et dolore magna.</p>
  </section>

  <footer class="copyright">© Copyright 2021. Learnway. All Rights Reserved.</footer>
</main>
</body>
</html>
```